Tallow Crest Business Card

We need a business card designed for a a company called "Tallow Crest". We offer consulting, coaching and training to business leaders and coaches (across the world) using the latest findings in neuroscience, social and emotional intelligence and positive psychology. The final design should communicate the use of brain science to create sustainable relationships.

The card should be doublesided. The logo is attached and names and titles will be provided to the successful designer. Thank you.

Industry/Entity Type

Training

```html
<!DOCTYPE html>
<html lang="en">
<head>
<meta charset="utf-8">
<title>Tallow Crest Business Card</title>
<link href="https://fonts.googleapis.com/css2?family=Marcellus&display=swap" rel="stylesheet">
<style>
  :root {
    --backdrop: #1b1b1c;
    --teal: #12c3c9;
    --lime: #c4fb0d;
    --sky: #7fd3ef;
    --mint: #cfeadc;
    --cream: #fdfcf4;
    --ink: #0d0d0d;
    --charcoal: #3f3f41;
    --name-blue: #5cc8f0;
    --edge: #2e3336;
  }
  html, body {
    margin: 0;
    padding: 0;
    width: 922px;
    height: 1200px;
    overflow: hidden;
    background: var(--backdrop);
  }
  .card {
    position: absolute;
    left: 41px;
    top: 305px;
    width: 840px;
    height: 590px;
    border-radius: 10px;
    overflow: hidden;
    background: linear-gradient(180deg, var(--sky) 0%, var(--mint) 45%, var(--cream) 100%);
    font-family: "Marcellus", serif;
  }
  .card__waves {
    position: absolute;
    inset: 0;
    width: 100%;
    height: 100%;
  }
  .brand {
    position: absolute;
    right: 38px;
    top: 40px;
    width: 300px;
    display: flex;
    flex-direction: column;
    align-items: center;
    gap: 14px;
  }
  .brand__dot {
    width: 86px;
    height: 86px;
    border-radius: 50%;
    background: var(--lime);
  }
  .brand__name {
    margin: 0;
    font-size: 50px;
    line-height: 1;
    color: var(--teal);
    font-weight: 400;
    white-space: nowrap;
  }
  .brand-mark {
    position: absolute;
    left: 22px;
    top: 468px;
    margin: 0;
    font-size: 32px;
    line-height: 1;
    color: var(--charcoal);
    font-weight: 400;
    white-space: nowrap;
  }
  .nameplate {
    position: absolute;
    left: 508px;
    top: 307px;
    width: 340px;
    height: 66px;
    box-sizing: border-box;
    padding: 4px 0 0 52px;
    background: var(--ink);
    border-radius: 12px;
    color: var(--name-blue);
  }
  .nameplate__name {
    margin: 0;
    font-size: 26px;
    line-height: 30px;
  }
  .nameplate__title {
    margin: 0 0 0 6px;
    font-size: 25px;
    line-height: 30px;
  }
  .contact-icon {
    position: absolute;
    left: 508px;
    width: 40px;
    height: 40px;
  }
  .contact-icon--home { top: 436px; }
  .contact-icon--mail { top: 490px; }
  .contact-icon--phone { top: 538px; left: 512px; width: 34px; height: 34px; }
</style>
</head>
<body>
  <main class="card">
    <svg class="card__waves" viewBox="0 0 648 455" preserveAspectRatio="none" aria-hidden="true">
      <path d="M0 0 H150 C130 40 118 80 130 120 C145 170 240 210 250 290 C258 360 210 420 188 455 H0 Z" fill="var(--teal)"/>
      <path d="M150 0 C130 40 118 80 130 120 C145 170 240 210 250 290 C258 360 210 420 188 455" fill="none" stroke="var(--edge)" stroke-width="1.5"/>
      <path d="M140 60 C128 110 150 150 190 190 C250 250 300 300 292 360 C285 410 250 440 238 455 H196 C222 425 268 380 268 330 C270 270 200 222 170 172 C150 136 138 100 140 60 Z" fill="var(--lime)"/>
    </svg>

    <div class="brand">
      <div class="brand__dot"></div>
      <p class="brand__name">Tallow Crest</p>
    </div>

    <p class="brand-mark">Tallow Crest</p>

    <div class="nameplate">
      <p class="nameplate__name">Your Name Here</p>
      <p class="nameplate__title">Title</p>
    </div>

    <svg class="contact-icon contact-icon--home" viewBox="0 0 24 24" aria-label="Address">
      <path d="M12 3 L2 12 H5 V21 H10 V15 H14 V21 H19 V12 H22 Z" fill="var(--ink)"/>
    </svg>
    <svg class="contact-icon contact-icon--mail" viewBox="0 0 24 24" aria-label="Email">
      <rect x="1" y="4" width="22" height="16" rx="2" fill="var(--ink)"/>
      <path d="M3 6.5 L12 13 L21 6.5 M3 18 L9.5 11.5 M21 18 L14.5 11.5" fill="none" stroke="#ffffff" stroke-width="1.2"/>
    </svg>
    <svg class="contact-icon contact-icon--phone" viewBox="0 0 24 24" aria-label="Phone">
      <circle cx="12" cy="12" r="10.5" fill="none" stroke="var(--ink)" stroke-width="1.8"/>
      <path d="M8.2 6.5 C7 7.3 6.8 9 7.6 10.8 C8.8 13.4 10.8 15.5 13.3 16.6 C15 17.3 16.5 17 17.3 15.8 L15.3 13.9 L13.8 14.9 C12 14 10.6 12.6 9.6 10.8 L10.6 9.3 Z" fill="var(--ink)"/>
    </svg>
  </main>
</body>
</html>
```